RM BIZ CARDS

Hi,

Is it possible to see a one sided version (with logo and info) as well as a two-sided version (front side w/logo and back side with info)?
How do we choose card stock and finish once we approve a design?

We would like the following info included:

Peter Lowell
Rosfeld Talent Media
4127 Marwick Lane, Suite 300
Los Angeles, CA 90041
(323) 555-0148
peter@rosfeldtalentmedia.example

```html
<!DOCTYPE html>
<html lang="en">
<head>
<meta charset="UTF-8">
<title>Rosfeld Talent Media – Business Cards</title>
<link rel="stylesheet" href="https://fonts.googleapis.com/css2?family=Lato:wght@300;400;700;900&display=swap">
<style>
  :root {
    --backdrop: #2b2b2b;
    --card: #ffffff;
    --card-shade: #ececec;
    --ink: #141414;
    --ink-soft: #2a2a2a;
  }
  * { margin: 0; padding: 0; box-sizing: border-box; }
  html, body {
    width: 1200px;
    height: 1031px;
    overflow: hidden;
    background: var(--backdrop);
    font-family: "Lato", sans-serif;
    color: var(--ink);
  }
  .sheet {
    position: relative;
    width: 1200px;
    height: 1031px;
  }
  .card {
    position: absolute;
    left: 260px;
    width: 680px;
    height: 389px;
    background: radial-gradient(ellipse at 40% 35%, var(--card) 55%, var(--card-shade) 100%);
    box-shadow: 0 18px 40px rgba(0,0,0,0.45);
  }
  .card--front { top: 90px; }
  .card--back { top: 552px; }

  /* Front */
  .brand {
    position: absolute;
    left: 0; right: 0;
    top: 150px;
    display: flex;
    align-items: center;
    justify-content: center;
    gap: 18px;
  }
  .brand__dot {
    width: 34px;
    height: 34px;
    border: 2px solid var(--ink);
    border-radius: 50%;
  }
  .brand__name {
    font-weight: 400;
    font-size: 30px;
    letter-spacing: 3px;
    text-transform: uppercase;
  }
  .front__web {
    position: absolute;
    left: 0; right: 0;
    bottom: 46px;
    text-align: center;
    font-size: 14px;
    font-weight: 400;
    letter-spacing: 9px;
    color: var(--ink-soft);
  }

  /* Back */
  .back__mark {
    position: absolute;
    right: 46px;
    top: 52px;
    display: flex;
    align-items: center;
    gap: 10px;
  }
  .back__mark .brand__dot { width: 28px; height: 28px; }
  .back__mark .brand__name { font-size: 26px; letter-spacing: 2px; }
  .back__rule {
    position: absolute;
    left: 250px;
    right: 0;
    top: 126px;
    height: 3px;
    background: var(--ink);
  }
  .person {
    position: absolute;
    left: 40px;
    top: 96px;
  }
  .person__name {
    font-weight: 900;
    font-size: 30px;
    text-transform: uppercase;
    line-height: 1;
    letter-spacing: -0.5px;
  }
  .person__company {
    font-size: 17px;
    font-weight: 400;
    margin-top: 6px;
  }
  .contact {
    position: absolute;
    left: 40px;
    bottom: 52px;
    font-size: 17px;
    line-height: 1.35;
    font-weight: 400;
    color: var(--ink-soft);
  }
  .address {
    position: absolute;
    right: 40px;
    top: 150px;
    text-align: right;
    font-size: 17px;
    line-height: 1.35;
    color: var(--ink-soft);
  }
</style>
</head>
<body>
<main class="sheet">
  <section class="card card--front" aria-label="Card front">
    <div class="brand">
      <span class="brand__dot"></span>
      <span class="brand__name">Rosfeld Talent</span>
    </div>
    <p class="front__web">rosfeldtalentmedia.example</p>
  </section>

  <section class="card card--back" aria-label="Card back">
    <div class="back__mark">
      <span class="brand__dot"></span>
      <span class="brand__name">RM</span>
    </div>
    <div class="back__rule"></div>
    <div class="person">
      <h1 class="person__name">Peter Lowell</h1>
      <p class="person__company">Rosfeld Talent Media</p>
    </div>
    <address class="address" style="font-style:normal">
      4127 Marwick Lane, Suite 300<br>
      Los Angeles, CA 90041
    </address>
    <p class="contact">
      (323) 555-0148<br>
      peter@rosfeldtalentmedia.example
    </p>
  </section>
</main>
</body>
</html>
```